Redesign Website - Current one too plain

The description is in the uploaded file. Please let me know if you need any more information. I'd prefer it if someone could implement the design to a WordPress site but the best design will win, regardless.
I would like the forms to look nice as well
UPDATE:
I don't think we can use the images that I provided, I think they make the site look a bit 'cheap' and I really don't know how to replace them. One thought I have had is to make the "Simple, Unique, Effective" a second feature on the right side of the page with the search on the left
Target Market(s)
Small companies, private sellers of cars and people who rent their caravan/holiday home out
Industry/Entity Type
Advertising
Number of Pages Required
3 page
Colors
Designer to choose colors to be used in the design.
Look and feel

```html
<!DOCTYPE html>
<html lang="en">
<head>
<meta charset="utf-8">
<title>KODIO.com – Find them by their code</title>
<link rel="stylesheet" href="https://fonts.googleapis.com/css2?family=Nunito:wght@400;600;700;800&family=Manrope:wght@400;500;700&display=swap">
<style>
:root{
  --ink:#0b0b0b;
  --nav-bg:#2e2e2f;
  --lime:#e6f700;
  --lime-soft:#cfe84a;
  --navy:#1b2550;
  --navy-deep:#111a3c;
  --field:#dfe0e5;
  --field-text:#3a3a3a;
  --white:#ffffff;
  --tile:#9a9a9a;
  --body:#2a2a2a;
}
*{box-sizing:border-box;margin:0;padding:0}
html,body{width:1200px;height:3372px;overflow:hidden;background:var(--white)}
body{font-family:"Manrope",sans-serif;color:var(--body);position:relative}
.page{position:relative;width:1200px;height:3372px}
.abs{position:absolute}
.brand{display:flex;align-items:center;gap:10px;font-family:"Nunito",sans-serif;font-weight:800;color:var(--lime);letter-spacing:2px}
.brand-dot{width:30px;height:30px;border-radius:50%;background:var(--lime)}

/* header */
.site-header{left:0;top:0;width:1200px;height:85px;background:var(--nav-bg)}
.site-header .brand{position:absolute;left:111px;top:22px;font-size:30px;height:40px}
.main-nav a,.footer-nav a{position:absolute;font-family:"Nunito",sans-serif;font-weight:700;font-size:17px;letter-spacing:1px;color:var(--white);text-decoration:none;white-space:nowrap}
.main-nav a{top:31px}

/* hero */
.hero{left:0;top:85px;width:1200px;height:600px;background:linear-gradient(100deg,#3a3b3d 0%,#2a2b2e 45%,#1d1e21 100%)}
.code-tile{width:97px;height:87px;top:151px;background:var(--tile);border-radius:4px;color:var(--white);font-family:"Nunito",sans-serif;font-weight:700;font-size:60px;display:flex;align-items:center;justify-content:center}
.spinner{top:178px;width:20px;height:30px}
.type-btn{top:282px;width:160px;height:56px;background:var(--white);border-radius:12px;font-family:"Nunito",sans-serif;font-weight:700;font-size:20px;letter-spacing:1.5px;color:#222;display:flex;align-items:center;justify-content:center}
.search-btn{left:512px;top:380px;width:177px;height:57px;background:var(--lime);border-radius:12px;font-family:"Nunito",sans-serif;font-weight:800;font-size:20px;letter-spacing:1.5px;color:#1a1a1a;display:flex;align-items:center;justify-content:center;gap:14px}

/* about */
.section-title{font-family:"Nunito",sans-serif;font-weight:800;font-size:31px;letter-spacing:2px;color:var(--ink)}
.about-title{left:111px;top:788px}
.about-text{left:111px;top:852px;width:470px;font-size:21.5px;line-height:38.6px;color:#333}
.btn-dark{background:var(--ink);color:var(--white);border-radius:12px;font-family:"Nunito",sans-serif;font-weight:800;letter-spacing:1.5px;display:flex;align-items:center;justify-content:center}
.learn-more{left:111px;top:1237px;width:235px;height:64px;font-size:23px}
.about-visual{left:600px;top:772px;width:488px;height:565px;border-radius:46% 54% 40% 60% / 40% 45% 55% 60%;background:radial-gradient(circle at 45% 40%,#e2f23a 0%,#b9d11f 45%,#7d9a12 100%)}

/* features */
.features{left:0;top:1425px;width:1200px;height:430px;background:linear-gradient(160deg,#24305e 0%,var(--navy) 40%,var(--navy-deep) 100%)}
.feature-card{top:62px;width:283px;height:302px;background:var(--white);border-radius:14px;text-align:center;padding-top:28px}
.feature-icon{width:80px;height:80px;margin:0 auto}
.feature-card h3{font-family:"Nunito",sans-serif;font-weight:800;font-size:24px;letter-spacing:2px;color:var(--ink);margin-top:10px}
.feature-card p{font-size:20.5px;line-height:38.6px;color:#333;margin-top:12px;padding:0 18px}
.flow-arrow{top:212px;width:64px;height:14px}

/* contact */
.contact-title{left:0;top:1941px;width:1200px;text-align:center}
.field{background:var(--field);border-radius:6px;font-size:16px;color:var(--field-text);padding-left:23px;display:flex;align-items:center}
.field.short{width:401px;height:51px}
.field.message{left:173px;top:2193px;width:856px;height:112px;align-items:flex-start;padding-top:20px}
.submit{left:538px;top:2344px;width:123px;height:50px;font-size:18px}

/* testimonials */
.testi-title{left:0;top:2476px;width:1200px;text-align:center}
.testi-card{top:2568px;width:478px;height:375px;background:var(--white);border-radius:10px;box-shadow:0 2px 10px rgba(0,0,0,.18);text-align:center}
.avatar{width:112px;height:112px;border-radius:50%;border:4px solid #8b8f96;margin:40px auto 0}
.testi-card h4{font-family:"Nunito",sans-serif;font-weight:800;font-size:21px;letter-spacing:2px;color:var(--ink);margin-top:22px}
.testi-card p{font-size:21px;line-height:38.6px;color:#333;margin-top:10px;padding:0 20px}
.slide-btn{top:2990px;width:44px;height:44px;border-radius:50%;background:var(--ink);display:flex;align-items:center;justify-content:center}

/* footer */
.site-footer{left:0;top:3122px;width:1200px;height:250px;background:var(--navy)}
.site-footer .brand{position:absolute;left:0;top:34px;width:1200px;justify-content:center;font-size:24px;gap:8px}
.site-footer .brand-dot{width:22px;height:22px}
.footer-nav a{top:95px}
.social{top:144px;width:26px;height:26px;border-radius:5px;background:#4a8ff0}
.copyright{left:0;top:193px;width:1200px;text-align:center;font-size:15px;font-weight:500;color:var(--white);letter-spacing:.3px}
</style>
</head>
<body>
<div class="page">

  <header class="site-header abs">
    <div class="brand"><span class="brand-dot"></span>KODIO.com</div>
    <nav class="main-nav">
      <a style="left:521px">HOME</a>
      <a style="left:636px">ABOUT US</a>
      <a style="left:787px">TESTIMONIALS</a>
      <a style="left:979px">CONTACT US</a>
    </nav>
  </header>

  <section class="hero abs" role="img" aria-label="Dusk photo of a modern office building with a caravan, a van and a car parked in front">
    <svg class="spinner abs" style="left:380px" viewBox="0 0 20 30"><path d="M4 11 L10 5 L16 11 M4 19 L10 25 L16 19" fill="none" stroke="#fff" stroke-width="2.2"/></svg>
    <div class="code-tile abs" style="left:433px">A</div>
    <div class="code-tile abs" style="left:571px">1</div>
    <svg class="spinner abs" style="left:696px" viewBox="0 0 20 30"><path d="M4 11 L10 5 L16 11 M4 19 L10 25 L16 19" fill="none" stroke="#fff" stroke-width="2.2"/></svg>
    <div class="type-btn abs" style="left:339px">CAR</div>
    <div class="type-btn abs" style="left:519px">CARAVAN</div>
    <div class="type-btn abs" style="left:702px">COMPANY</div>
    <div class="search-btn abs">SEARCH
      <svg width="22" height="22" viewBox="0 0 22 22"><circle cx="9" cy="9" r="7" fill="none" stroke="#1a1a1a" stroke-width="2.4"/><path d="M14 14 L20 20" stroke="#1a1a1a" stroke-width="2.4" stroke-linecap="round"/></svg>
    </div>
  </section>

  <section class="about">
    <h2 class="section-title abs about-title">ABOUT US</h2>
    <p class="about-text abs">Sed ut perspiciatis unde omnis iste natus error sit voluptatem accusantium doloremque laudantium, totam rem aperiam, eaque ipsa quae ab illo inventore veritatis et quasi architecto beatae vitae dicta sunt explicabo. Nemo enim ipsam voluptatem quia voluptas sit aspernatur aut odit aut fugit, sed quia consequuntur magni dolores eos qui ratione voluptatem sequi nesciunt.</p>
    <div class="btn-dark learn-more abs">LEARN MORE</div>
    <div class="about-visual abs" role="img" aria-label="Lime-tinted photo of a glass office building inside a paint splash shape"></div>
  </section>

  <section class="features abs">
    <div class="feature-card abs" style="left:113px">
      <svg class="feature-icon" viewBox="0 0 80 80"><circle cx="40" cy="40" r="30" fill="var(--lime-soft)" opacity=".7"/><circle cx="38" cy="42" r="18" fill="none" stroke="#111" stroke-width="2.5"/><circle cx="38" cy="42" r="11" fill="none" stroke="#111" stroke-width="2.5"/><circle cx="38" cy="42" r="4" fill="#111"/><path d="M38 42 L60 22 M54 20 L60 22 L58 28" fill="none" stroke="#111" stroke-width="2.5"/></svg>
      <h3>SIMPLE</h3>
      <p>create &nbsp;your advert and display your code</p>
    </div>
    <svg class="flow-arrow abs" style="left:396px" viewBox="0 0 64 14"><path d="M0 7 H60" stroke="#fff" stroke-width="1" stroke-dasharray="2 2"/><path d="M54 2 L60 7 L54 12" fill="none" stroke="#fff" stroke-width="1.6"/></svg>
    <div class="feature-card abs" style="left:459px;top:63px">
      <svg class="feature-icon" viewBox="0 0 80 80"><circle cx="40" cy="40" r="30" fill="var(--lime-soft)" opacity=".7"/><circle cx="36" cy="36" r="16" fill="none" stroke="#111" stroke-width="2.5"/><circle cx="36" cy="36" r="10" fill="none" stroke="#111" stroke-width="2"/><circle cx="36" cy="36" r="4" fill="none" stroke="#111" stroke-width="2"/><path d="M48 48 L60 60" stroke="#111" stroke-width="4" stroke-linecap="round"/></svg>
      <h3 style="margin-top:0">UNIQUE</h3>
      <p style="margin-top:8px">customers find you by an easy-to-remember code</p>
    </div>
    <svg class="flow-arrow abs" style="left:742px" viewBox="0 0 64 14"><path d="M0 7 H60" stroke="#fff" stroke-width="1" stroke-dasharray="2 2"/><path d="M54 2 L60 7 L54 12" fill="none" stroke="#fff" stroke-width="1.6"/></svg>
    <div class="feature-card abs" style="left:804px;top:63px">
      <svg class="feature-icon" viewBox="0 0 80 80"><circle cx="40" cy="40" r="30" fill="var(--lime-soft)" opacity=".7"/><circle cx="36" cy="42" r="12" fill="none" stroke="#111" stroke-width="2.5" stroke-dasharray="5 3"/><circle cx="36" cy="42" r="5" fill="none" stroke="#111" stroke-width="2.5"/><circle cx="54" cy="48" r="8" fill="none" stroke="#111" stroke-width="2.5"/><path d="M54 44 V48 H57 M42 24 V12 M38 16 L42 12 L46 16 M50 28 L58 20" fill="none" stroke="#111" stroke-width="2.2"/></svg>
      <h3 style="margin-top:0">EFFECTIVE</h3>
      <p style="margin-top:6px">customers are directed to you and not a list of your competitors</p>
    </div>
  </section>

  <section class="contact">
    <h2 class="section-title abs contact-title">CONTACT US</h2>
    <div class="field short abs" style="left:173px;top:2025px">First Name</div>
    <div class="field short abs" style="left:627px;top:2025px">Last Name</div>
    <div class="field short abs" style="left:173px;top:2109px">Phone Number</div>
    <div class="field short abs" style="left:627px;top:2109px">Email Address</div>
    <div class="field message abs">Enter Your Message....</div>
    <div class="btn-dark submit abs">SUBMIT</div>
  </section>

  <section class="testimonials">
    <h2 class="section-title abs testi-title">TESTIMONIALS</h2>
    <article class="testi-card abs" style="left:111px">
      <div class="avatar" role="img" aria-label="Portrait of a smiling woman in an orange shirt" style="background:linear-gradient(180deg,#7fb6d6 0%,#e0733a 100%)"></div>
      <h4>LOREM IPISUM</h4>
      <p>Ut enim ad minima veniam, quis nostrum exercitationem ullam corporis suscipit laboriosam, nisi ut aliquid ex ea commodi</p>
    </article>
    <article class="testi-card abs" style="left:610px">
      <div class="avatar" role="img" aria-label="Portrait of a smiling man in a black shirt" style="background:linear-gradient(180deg,#e9e9ea 0%,#2a2a2c 100%)"></div>
      <h4>LOREM IPISUM</h4>
      <p>Ut enim ad minima veniam, quis nostrum exercitationem ullam corporis suscipit laboriosam, nisi ut aliquid ex ea commodi</p>
    </article>
    <div class="slide-btn abs" style="left:544px"><svg width="14" height="14" viewBox="0 0 14 14"><path d="M9 2 L4 7 L9 12" fill="none" stroke="#fff" stroke-width="2"/></svg></div>
    <div class="slide-btn abs" style="left:613px"><svg width="14" height="14" viewBox="0 0 14 14"><path d="M5 2 L10 7 L5 12" fill="none" stroke="#fff" stroke-width="2"/></svg></div>
  </section>

  <footer class="site-footer abs">
    <div class="brand"><span class="brand-dot"></span>KODIO.com</div>
    <nav class="footer-nav">
      <a style="left:340px">HOME</a>
      <a style="left:439px">ABOUT US</a>
      <a style="left:573px">TESTIMONIALS</a>
      <a style="left:747px">CONTACT US</a>
    </nav>
    <span class="social abs" style="left:547px"></span>
    <span class="social abs" style="left:587px"></span>
    <span class="social abs" style="left:626px"></span>
    <p class="copyright abs">@2023 COPYRIGHTS. KODIO. ALL RIGHTS RESERVED.</p>
  </footer>

</div>
</body>
</html>
```